Lumora business card for a plastic surgeon

we need a business card for plastic surgeons that work on a clinic called LUMORA.
we want a clean design and the following informations: name of the doctor, doctor's registration number (called CRM), telephone, address, facebook, instagram.
Colors: white, blue tones, light brown/ coffee

facebook and instagram: lumoracirurgiaestetica

Industry/Entity Type

Business

Contact Information for Business Card

clean design

Font styles to use
Serif
Sans Serif
Other font styles liked:
• helvetica light

Colors
cee9f5
85cae6
85abd2
3276b5
cfeae6
cedeed
eaf1f7

Requirements
Must have
• doctor's name
• identification number (called CRM)
• contact (phone, facebook, instagram, address)

```html
<!DOCTYPE html>
<html lang="pt">
<head>
<meta charset="utf-8">
<title>Lumora – Business Card</title>
<link rel="stylesheet" href="https://fonts.googleapis.com/css2?family=Lato:wght@300;400;700;900&display=swap">
<style>
  :root {
    --bg: #e6e9ed;
    --white: #ffffff;
    --navy: #17355e;
    --cyan: #1bb3d9;
    --sky: #85cae6;
    --sky-pale: #cee9f5;
    --sky-mist: #eaf1f7;
    --brand: #29a9d6;
    --ink: #1e3a66;
  }
  * { box-sizing: border-box; margin: 0; padding: 0; }
  html, body { width: 1200px; height: 1000px; overflow: hidden; }
  body {
    background: var(--bg);
    font-family: 'Lato', Arial, sans-serif;
    position: relative;
  }
  .card {
    position: absolute;
    top: 200px;
    width: 340px;
    height: 595px;
    background: var(--white);
    overflow: hidden;
    box-shadow: 0 14px 34px rgba(20, 40, 70, 0.22);
  }
  .card--front { left: 210px; }
  .card--back { left: 650px; }
  .card__pattern { position: absolute; inset: 0; width: 100%; height: 100%; }

  .brand {
    position: absolute;
    left: 0; right: 0;
    display: flex;
    align-items: center;
    justify-content: center;
    gap: 12px;
  }
  .brand__dot {
    width: 14px; height: 14px;
    border-radius: 50%;
    background: var(--brand);
  }
  .brand__name {
    font-weight: 400;
    font-size: 54px;
    letter-spacing: 3px;
    color: var(--brand);
  }
  .card--front .brand { top: 100px; }
  .card--back .brand { top: 205px; }

  .card__panel {
    position: absolute;
    left: 0; right: 0; bottom: 0;
    height: 285px;
    background: var(--navy);
    border-top: 14px solid var(--cyan);
    color: var(--white);
    padding: 30px 20px 0 30px;
  }
  .info-block {
    border-left: 5px solid var(--cyan);
    padding-left: 22px;
  }
  .person__name { font-size: 23px; font-weight: 300; letter-spacing: 0.5px; line-height: 1.15; }
  .person__name strong { font-weight: 900; }
  .person__role { font-size: 15px; font-weight: 300; margin-top: 3px; opacity: 0.9; }
  .person__crm { font-size: 13px; font-weight: 700; margin-top: 3px; letter-spacing: 0.4px; color: var(--sky-pale); }

  .contact { margin-top: 24px; }
  .contact__row {
    display: flex;
    align-items: flex-start;
    gap: 10px;
    font-size: 15px;
    line-height: 1.25;
    margin-bottom: 8px;
  }
  .contact__row:last-child { margin-bottom: 0; }
  .contact__row svg { flex: none; width: 16px; height: 16px; margin-top: 2px; fill: var(--white); }
  .contact__row--address { font-weight: 700; }

  .social {
    position: absolute;
    left: 0; right: 0; top: 292px;
    display: flex;
    flex-direction: column;
    align-items: center;
    gap: 10px;
  }
  .social__mark { width: 26px; height: 26px; background: var(--ink); border-radius: 3px; }
  .social__handle { font-size: 14px; font-weight: 700; color: var(--ink); letter-spacing: 0.2px; }
</style>
</head>
<body>

  <section class="card card--front" aria-label="Front of business card">
    <svg class="card__pattern" viewBox="0 0 340 595" aria-hidden="true">
      <polygon points="0,280 340,130 340,310 0,310" fill="var(--sky-pale)" opacity="0.6"/>
      <polygon points="0,240 340,220 340,310 0,310" fill="var(--sky-mist)" opacity="0.8"/>
      <polygon points="120,310 340,180 340,310" fill="var(--sky-pale)" opacity="0.7"/>
    </svg>

    <div class="brand">
      <span class="brand__dot"></span>
      <span class="brand__name">LUMORA</span>
    </div>

    <div class="card__panel">
      <div class="info-block person">
        <p class="person__name"><strong>YOUR</strong> NAME</p>
        <p class="person__role">Cirurgião Plástico</p>
        <p class="person__crm">CRM-SP 123456</p>
      </div>

      <div class="info-block contact">
        <p class="contact__row contact__row--address">
          <svg viewBox="0 0 16 16"><path d="M8 0a5.5 5.5 0 0 0-5.5 5.5C2.5 9.6 8 16 8 16s5.5-6.4 5.5-10.5A5.5 5.5 0 0 0 8 0zm0 8a2.5 2.5 0 1 1 0-5 2.5 2.5 0 0 1 0 5z"/></svg>
          <span>Rua das Acácias, 210<br>São Paulo SP 01234-000</span>
        </p>
        <p class="contact__row">
          <svg viewBox="0 0 16 16"><path d="M3.5 1.5l2.5 0 1 3.5-1.8 1.2a9 9 0 0 0 4.6 4.6L11 9l3.5 1v2.5c0 1-1 2-2 2C6.5 14.5 1.5 9.5 1.5 3.5c0-1 1-2 2-2z"/></svg>
          <span>+55 11 4000 . 2718<br>lumora@email.com</span>
        </p>
        <p class="contact__row">
          <svg viewBox="0 0 16 16"><path d="M8 0a8 8 0 1 0 0 16A8 8 0 0 0 8 0zm5.9 7h-2.5a12 12 0 0 0-1-4.7A6 6 0 0 1 13.9 7zM8 2c.8 1 1.4 2.9 1.5 5h-3C6.6 4.9 7.2 3 8 2zM5.6 2.3A12 12 0 0 0 4.6 7H2.1a6 6 0 0 1 3.5-4.7zM2.1 9h2.5a12 12 0 0 0 1 4.7A6 6 0 0 1 2.1 9zM8 14c-.8-1-1.4-2.9-1.5-5h3c-.1 2.1-.7 4-1.5 5zm2.4-.3a12 12 0 0 0 1-4.7h2.5a6 6 0 0 1-3.5 4.7z"/></svg>
          <span>www.lumora.com</span>
        </p>
      </div>
    </div>
  </section>

  <section class="card card--back" aria-label="Back of business card">
    <svg class="card__pattern" viewBox="0 0 340 595" aria-hidden="true">
      <polygon points="0,0 340,0 340,120 0,170" fill="var(--sky-pale)"/>
      <polygon points="0,0 200,0 0,150" fill="var(--sky)" opacity="0.45"/>
      <polygon points="200,0 340,0 340,120 260,130" fill="var(--sky)" opacity="0.3"/>
      <polygon points="0,440 340,420 340,595 0,595" fill="var(--sky-pale)"/>
      <polygon points="340,300 340,595 150,595" fill="var(--sky)" opacity="0.45"/>
      <polygon points="0,440 140,440 0,595" fill="var(--sky)" opacity="0.3"/>
      <polygon points="340,120 340,330 250,125" fill="var(--sky-pale)" opacity="0.8"/>
    </svg>

    <div class="brand">
      <span class="brand__dot"></span>
      <span class="brand__name">LUMORA</span>
    </div>

    <div class="social">
      <span class="social__mark"></span>
      <span class="social__handle">lumoracirurgiaestetica</span>
    </div>
  </section>

</body>
</html>
```